We sincerely appreciate everyone's interest in our website design project. In all we had 65 designs submitted and were amazed by the creativity and quality presented. Unfortunately, as with all contests, there can only be one winner and the winning firm was selected at 12:00 ET 7/7/2017. We wish you all the best and look forward to potentially working with you on future projects. Thanks again for your time and interests. Tobin

Thanks for your interest in our project! Due to the overwhelming number of submissions received, additional submissions will not be accepted after close of business 7/4. Additionally, to minimize unnecessary additional work, we will begin reviewing all submissions received on 7/5, select the submission(s) that come closest to meeting our needs and work with the designer(s) selected to finalize their designs. Thanks again.

Thanks for the feedback!!

Based on feedback provided, we understand that the initial specifications required that the site be developed as dynamic versus static and, as such, the budget was insufficient. With this in mind, we have modified the specifications as follows:
1. Clean, simple, uncluttered site
2. 4-5 pages consisting of the following:
a. Home page
b. About us
c. Services provided
d. Contact us/request quote/request service
2. No people in pools/photos unless it involves cleaning i.e., vacuuming, netting, etc.

We are in need of a website to promote our business and the services provided to our customers. The site should be a simple 5 page design providing information about us, the services we provide, our service territory (Central Florida = Seminole and Orange Counties), the ability to request a service quote, the ability to schedule service, the ability to pay invoices, the ability to refer neighbors and friends, the ability to leave reviews and provide feedback, etc. We are a certified, licensed, and insured veteran minority owned and operated company with 10 years industry experience providing unparalleled commercial and residential pool and spa care in the central Florida area. While we are seeking something more impressive and concise, an example of the site would be http://marlowpoolservice.example/ OR http://www.bluefinchpoolcompany.example/

Target Market(s)

Hotels, motels, apartment complexes, condominium associations, homeowners associations, and individual homeowners

Industry/Entity Type

It Company

Contact Information for Business Card

Logo, name, phone number, website, "Certified Licensed Insured", "Providing quality pool care to Central Florida"

Coding

Coded - Design and coding required

Number of Pages Required

5+ page

Requirements
Must have
• See description
Nice to have
• See description
Should not have
• See description

```html
<!DOCTYPE html>
<html lang="en">
<head>
<meta charset="utf-8">
<title>Tidewell Aquatics</title>
<link href="https://fonts.googleapis.com/css2?family=Arimo:wght@400;700&family=PT+Sans:wght@400;700&family=PT+Sans+Narrow:wght@400;700&display=swap" rel="stylesheet">
<style>
:root{
  --blue:#2f6aa8;
  --blue-dark:#245a92;
  --orange:#f47b12;
  --rust:#b4520f;
  --yellow:#f6c21c;
  --ink:#333333;
  --text:#444444;
  --grey-band:#f0f0f0;
  --footer:#f3f3f3;
  --footer-bar:#e6e6e6;
  --line:#dddddd;
  --link:#2f6aa8;
  --white:#ffffff;
}
*{margin:0;padding:0;box-sizing:border-box}
html,body{width:1200px;height:2343px;overflow:hidden}
body{position:relative;background:var(--white);font-family:"Arimo",Arial,sans-serif;color:var(--text)}
.abs{position:absolute}

/* header */
.site-header{position:absolute;left:0;top:0;width:1200px;height:108px;background:var(--white)}
.brand{position:absolute;left:192px;top:26px;display:flex;align-items:center;gap:12px;font-family:"PT Sans",sans-serif;font-weight:700;font-size:30px;color:var(--blue);line-height:1}
.brand-mark{width:34px;height:34px;border-radius:50%;background:var(--orange)}
.header-phone{position:absolute;right:91px;top:46px;font-family:"Arimo",sans-serif;font-weight:700;font-size:19px;color:var(--rust)}

.main-nav{position:absolute;left:0;top:108px;width:1200px;height:35px;background:var(--blue);border-bottom:3px solid var(--blue-dark)}
.main-nav a{position:absolute;top:9px;color:var(--white);text-decoration:none;font-family:"Arimo",sans-serif;font-weight:700;font-size:13px;letter-spacing:1.8px}

/* hero */
.hero{position:absolute;left:0;top:143px;width:1200px;height:360px;background:linear-gradient(180deg,#b9d6e8 0%,#7fb5d6 22%,#4c9fd0 45%,#2f8fc8 70%,#5fb3de 100%)}
.hero-title{position:absolute;left:698px;top:88px;font-family:"PT Sans Narrow",sans-serif;font-weight:700;font-size:31px;color:var(--white);letter-spacing:.5px}
.hero-sub{position:absolute;left:698px;top:130px;font-family:"PT Sans Narrow",sans-serif;font-weight:700;font-size:21px;color:var(--yellow);letter-spacing:.5px}
.hero-text{position:absolute;left:698px;top:178px;width:360px;font-size:12px;line-height:19px;color:var(--yellow)}
.hero-btn{position:absolute;left:698px;top:247px;width:170px;height:38px;background:var(--orange);color:var(--white);font-weight:700;font-size:15px;line-height:38px;text-align:center}
.hero-dots{position:absolute;left:564px;top:330px;display:flex;gap:3px}
.hero-dots span{width:10px;height:10px;background:#9aa7b0;border:1px solid #fff}
.hero-dots span.on{background:#111}

/* services */
.service{position:absolute;width:420px;text-align:center}
.service-num{width:56px;height:56px;margin:0 auto;border:1.5px solid var(--ink);border-radius:50%;font-family:"PT Sans",sans-serif;font-size:18px;line-height:53px;color:var(--ink)}
.service-title{margin-top:24px;font-family:"PT Sans",sans-serif;font-weight:400;font-size:20px;color:var(--ink);letter-spacing:.3px}
.service-text{margin-top:8px;font-size:12.5px;line-height:21px;color:var(--text)}
.service-divider{position:absolute;left:192px;top:846px;width:826px;height:1px;background:#e8e8e8}

/* about */
.about{position:absolute;left:0;top:1095px;width:1200px;height:454px;background:var(--grey-band)}
.section-title{font-family:"PT Sans",sans-serif;font-size:25px;color:var(--ink);font-weight:400}
.about p{font-size:12.5px;line-height:21px;color:var(--ink)}
.about-img{position:absolute;left:618px;top:174px;width:400px;height:249px;background:linear-gradient(180deg,#2f6fb8 0%,#8fbde3 40%,#dfeef8 55%,#4bb2e3 75%,#1f8ccf 100%)}

/* contact + gallery */
.field{position:absolute;left:192px;width:267px;height:35px;border:1px solid #cfcfcf;background:var(--white);font-size:11.5px;color:#777;padding:11px 0 0 18px}
.field-message{width:261px;height:135px;border:1px solid #999;padding:4px 0 0 2px;font-family:"Courier New",monospace;color:#888}
.submit-btn{position:absolute;left:192px;top:1960px;width:93px;height:34px;background:#000;border-radius:4px;color:var(--white);font-weight:700;font-size:12px;line-height:34px;text-align:center}
.gallery-img{position:absolute;left:477px;top:1656px;width:536px;height:335px;background:linear-gradient(180deg,#2a68b5 0%,#9cc6e8 38%,#e6f2fa 52%,#48aee2 72%,#1a86cc 100%)}
.gallery-dots{position:absolute;left:896px;top:1989px;display:flex;gap:4px}
.gallery-dots span{width:11px;height:11px;border-radius:50%;background:#777}
.gallery-dots span.on{background:var(--white);border:1px solid #888}

/* footer */
.site-footer{position:absolute;left:0;top:2076px;width:1200px;height:226px;background:var(--footer)}
.foot-col{position:absolute;top:26px;width:182px}
.foot-col h4{font-family:"PT Sans",sans-serif;font-weight:400;font-size:15px;color:var(--orange);padding-bottom:6px;border-bottom:1px solid var(--line)}
.foot-col p{margin-top:12px;font-size:12.5px;line-height:21px;color:var(--ink)}
.foot-links li{list-style:none;height:37px;border-bottom:1px solid var(--line);display:flex;align-items:center;gap:6px;font-size:12.5px;color:var(--link)}
.foot-links{margin-top:2px}
.news-title{margin-top:12px;font-size:15px;color:var(--link)}
.news-meta{font-size:9.5px;color:#555;margin-top:3px}
.news-meta span{color:var(--link)}
.news-text{margin-top:3px!important;width:172px;font-size:12px!important;line-height:18px!important;padding-bottom:6px;border-bottom:1px solid var(--line)}
.foot-bar{position:absolute;left:0;top:2302px;width:1200px;height:41px;background:var(--footer-bar);font-size:12px;color:#555}
.foot-bar .copy{position:absolute;left:184px;top:14px}
.foot-bar .top-link{position:absolute;left:960px;top:14px;color:var(--blue);text-decoration:underline}
</style>
</head>
<body>

<header class="site-header">
  <div class="brand"><span class="brand-mark"></span>Tidewell Aquatics</div>
  <div class="header-phone">Call Us Free: 1-800-555-0199</div>
</header>

<nav class="main-nav">
  <a style="left:190px">HOME</a>
  <a style="left:313px">ABOUT US</a>
  <a style="left:469px">PRODUCTS</a>
  <a style="left:631px">CONTACT US</a>
</nav>

<section class="hero">
  <div class="abs" role="img" aria-label="Sparkling blue swimming pool with steel ladder rails beside the sea" style="inset:0"></div>
  <div class="hero-title">TIDEWELL</div>
  <div class="hero-sub">AQUATIC SERVICE !</div>
  <div class="hero-text">We keep your pool clean, balanced and sparkling all year, so you can relax and enjoy every sunny Florida day with family.</div>
  <div class="hero-btn">View all Services</div>
  <div class="hero-dots"><span class="on"></span><span></span><span></span><span></span><span></span></div>
</section>

<section class="services">
  <div class="service" style="left:182px;top:596px">
    <div class="service-num">01</div>
    <h3 class="service-title">DESIGN &amp; CONSTRUCTION</h3>
    <p class="service-text">Our mission is to enhance your pool and spa experience so that you<br>may enjoy a healthier and happier life. Our goal is your satisfaction!</p>
  </div>
  <div class="service" style="left:606px;top:596px">
    <div class="service-num">02</div>
    <h3 class="service-title">SWIMMING POOL &amp; SPA REPAIR</h3>
    <p class="service-text">We will help you select a pool that's right for your needs and your<br>budget. Choose from hundreds of proven designs, or, if you wish, we'll<br>design a pool that's as unique as you are.</p>
  </div>
  <div class="service-divider"></div>
  <div class="service" style="left:182px;top:878px">
    <div class="service-num">03</div>
    <h3 class="service-title">MAINTENANCE &amp; WATER TREATMENT</h3>
    <p class="service-text">We'll show you how to plan your pool for maximum enjoyment, making<br>the best use of available sunlight, existing foliage and natural<br>windbreaks.</p>
  </div>
  <div class="service" style="left:606px;top:878px">
    <div class="service-num">04</div>
    <h3 class="service-title">ENVIRONMENTAL SOLUTIONS</h3>
    <p class="service-text">Members have amassed an impressive list of new breakthroughs and<br>awards. And we are not done yet. Innovation is more than just a great<br>idea.</p>
  </div>
</section>

<section class="about">
  <h2 class="section-title abs" style="left:192px;top:43px">About Us</h2>
  <p class="abs" style="left:192px;top:80px;width:826px">Tidewell Aquatic Service is Florida's premier swimming pool service and repair company, serving Florida for over 26 years!<br>Customer service is our specialty. With the large number of swimming pool service companies in Florida, there are a lot of choices available for consumers. At Tidewell Aquatic Service, we believe our unparalleled customer service sets us apart from the competition. We provide a high-quality service at a fair price with a 100% Satisfaction Guarantee.</p>
  <p class="abs" style="left:192px;top:178px;width:395px">Tidewell Aquatic Service is Florida's premier swimming pool service and repair company, serving Florida for over 26 years!<br>Customer service is our specialty. With the large number of swimming pool service companies in Florida, there are a lot of choices available for consumers. At Tidewell Aquatic Service, we believe our unparalleled customer service sets us apart from the competition. We provide a high-quality service at a fair price with a 100% Satisfaction Guarantee.</p>
  <p class="abs" style="left:192px;top:364px;width:395px">Tidewell Aquatic Service is Florida's premier swimming pool service and repair company, serving Florida for over 26 years!</p>
  <div class="about-img" role="img" aria-label="Infinity pool with ladder under a bright sunny sky"></div>
</section>

<section class="contact">
  <h2 class="section-title abs" style="left:192px;top:1594px">Contact Us</h2>
  <h2 class="section-title abs" style="left:477px;top:1594px">Photo Gallery</h2>
  <div class="field" style="top:1669px">Enter Name</div>
  <div class="field" style="top:1713px">Enter Email</div>
  <div class="field" style="top:1757px">Enter Subject</div>
  <div class="field field-message" style="top:1801px">Enter Message</div>
  <div class="submit-btn">Submit</div>
  <div class="gallery-img" role="img" aria-label="Gallery photo of a blue infinity pool under a sunny sky"></div>
  <div class="gallery-dots"><span class="on"></span><span></span><span></span><span></span><span></span></div>
</section>

<footer class="site-footer">
  <div class="foot-col" style="left:192px">
    <h4>About Us</h4>
    <p>Tidewell Aquatic Service is Florida's premier swimming pool service and repair company, serving Florida for over 26 years!</p>
  </div>
  <div class="foot-col" style="left:406px">
    <h4>Quick Links</h4>
    <ul class="foot-links">
      <li><svg width="9" height="8" viewBox="0 0 9 8"><path d="M1 1l3 3-3 3M5 1l3 3-3 3" fill="none" stroke="#888" stroke-width="1.2"/></svg>Home</li>
      <li><svg width="9" height="8" viewBox="0 0 9 8"><path d="M1 1l3 3-3 3M5 1l3 3-3 3" fill="none" stroke="#888" stroke-width="1.2"/></svg>About Us</li>
      <li><svg width="9" height="8" viewBox="0 0 9 8"><path d="M1 1l3 3-3 3M5 1l3 3-3 3" fill="none" stroke="#888" stroke-width="1.2"/></svg>Products</li>
      <li><svg width="9" height="8" viewBox="0 0 9 8"><path d="M1 1l3 3-3 3M5 1l3 3-3 3" fill="none" stroke="#888" stroke-width="1.2"/></svg>Contact Us</li>
    </ul>
  </div>
  <div class="foot-col" style="left:620px">
    <h4>Latest News</h4>
    <div class="news-title">Hello world!</div>
    <div class="news-meta">June 29, 2017 by <span>admin</span></div>
    <p class="news-text">Welcome to SitePress. This is<br>your first post. Edit or delete it,<br>then…</p>
  </div>
  <div class="foot-col" style="left:834px">
    <h4>Contact Us</h4>
    <p>Tidewell Aquatic Service Co.<br>P.O. Box 40712 Lakeview,<br>Florida 32790<br>Phone: (407) 555-0148</p>
  </div>
</footer>

<div class="foot-bar">
  <span class="copy">© 2017 <b>Tidewell Aquatics</b></span>
  <span class="top-link">Back to Top</span>
</div>

</body>
</html>
```